Fernbrook Dwellings Business Card Design Project

Please create a custom Business Card Design for Fernbrook Dwellings. The logo is attached to this brief.Please include space for
Name Surname
Title (Solutions Specialist)
Phone
Email
Website
Industry/Entity Type
Business
Contact Information for Business Card
Reverse should be printed horizontally and have the following components:
Small version of the logo. (lowest priority)
The words "Real Estate Solutions Company"
A bulleted list (Note: Line breaks are suggestions only):
* BUY, RENOVATE, SELL and RENT:
RESIDENTIAL PROPERTIES
* MAKE CASH OFFERS ON HOUSES IN
ANY CONDITION and IN ANY SITUATION
* SELL PROPERTIES TO INVESTORS
* SOLVE COMPLEX REAL ESTATE
PROBLEMS and TITLE ISSUES
* PRIVATE MONEY INVESTMENT SERVICES
* PAY CASH REWARDS FOR REFERRALS
Included somewhere on the reverse should also be the following:
Office: (425) 555-0183
www.FernbrookDwellings.example
space for civic trade registry logo
Look and feel
Each slider illustrates characteristics of the customer's brand and the style your logo design should communicate.

```html
<!DOCTYPE html>
<html lang="en">
<head>
<meta charset="utf-8">
<title>Fernbrook Dwellings – Business Card</title>
<link rel="stylesheet" href="https://fonts.googleapis.com/css2?family=Questrial&display=swap">
<style>
  :root {
    --brand-blue: #0b5aa2;
    --brand-yellow: #f7c600;
    --card-white: #ffffff;
    --card-edge: #8a8a8a;
    --page-bg: #ffffff;
    --band-text: #ffffff;
  }
  * { box-sizing: border-box; margin: 0; padding: 0; }
  html, body {
    width: 1200px;
    height: 686px;
    overflow: hidden;
    background: var(--page-bg);
  }
  body {
    font-family: "Questrial", "Century Gothic", sans-serif;
    color: var(--brand-blue);
  }
  .card-sheet {
    position: relative;
    width: 1200px;
    height: 686px;
  }
  .card {
    position: absolute;
    top: 190px;
    width: 551px;
    height: 306px;
    background: var(--card-white);
    border: 1px solid var(--card-edge);
    overflow: hidden;
  }
  .card--front { left: 44px; }
  .card--back  { left: 605px; }
  .card__band {
    position: absolute;
    left: 0;
    right: 0;
    bottom: 0;
    height: 31px;
    background: var(--brand-blue);
    display: flex;
    align-items: center;
    justify-content: center;
    gap: 28px;
    color: var(--band-text);
    font-size: 13px;
    letter-spacing: 0.3px;
  }

  /* Front: wordmark, company line and services */
  .brand-lockup {
    position: absolute;
    left: 0;
    right: 0;
    top: 16px;
    display: flex;
    flex-direction: column;
    align-items: center;
  }
  .brand-lockup__dot {
    width: 34px;
    height: 34px;
    border-radius: 50%;
    background: var(--brand-yellow);
    margin-bottom: 6px;
  }
  .brand-lockup__name {
    font-size: 24px;
    line-height: 1.1;
    letter-spacing: 0.5px;
  }
  .company-line {
    position: absolute;
    left: 0;
    right: 0;
    top: 96px;
    text-align: center;
    font-size: 14px;
    letter-spacing: 2px;
    text-transform: uppercase;
  }
  .service-list {
    position: absolute;
    left: 26px;
    top: 124px;
    width: 440px;
    columns: 2;
    column-gap: 18px;
    list-style: none;
    font-size: 10px;
    line-height: 13px;
  }
  .service-list li {
    position: relative;
    padding-left: 10px;
    margin-bottom: 6px;
    break-inside: avoid;
  }
  .service-list li::before {
    content: "";
    position: absolute;
    left: 0;
    top: 4px;
    width: 4px;
    height: 4px;
    border-radius: 50%;
    background: var(--brand-yellow);
  }
  .registry-space {
    position: absolute;
    right: 24px;
    top: 200px;
    width: 40px;
    height: 40px;
    border: 1px solid var(--brand-blue);
  }

  /* Back: contact labels and small wordmark */
  .contact-list {
    position: absolute;
    left: 63px;
    top: 50px;
    list-style: none;
    font-size: 24px;
    line-height: 33px;
  }
  .brand-mini {
    position: absolute;
    top: 16px;
    right: 24px;
    display: flex;
    flex-direction: column;
    align-items: center;
  }
  .brand-mini__dot {
    width: 32px;
    height: 32px;
    border-radius: 50%;
    background: var(--brand-yellow);
    margin-bottom: 8px;
  }
  .brand-mini__name {
    font-size: 13px;
    line-height: 1.15;
    text-align: center;
  }
</style>
</head>
<body>
<main class="card-sheet">
  <section class="card card--front" aria-label="Card reverse">
    <div class="brand-lockup">
      <span class="brand-lockup__dot" aria-hidden="true"></span>
      <span class="brand-lockup__name">Fernbrook Dwellings</span>
    </div>
    <p class="company-line">Real Estate Solutions Company</p>
    <ul class="service-list">
      <li>BUY, RENOVATE, SELL and RENT: RESIDENTIAL PROPERTIES</li>
      <li>MAKE CASH OFFERS ON HOUSES IN ANY CONDITION and IN ANY SITUATION</li>
      <li>SELL PROPERTIES TO INVESTORS</li>
      <li>SOLVE COMPLEX REAL ESTATE PROBLEMS and TITLE ISSUES</li>
      <li>PRIVATE MONEY INVESTMENT SERVICES</li>
      <li>PAY CASH REWARDS FOR REFERRALS</li>
    </ul>
    <div class="registry-space" role="img" aria-label="Space for civic trade registry badge"></div>
    <div class="card__band">
      <span>Office: (425) 555-0183</span>
      <span>www.FernbrookDwellings.example</span>
    </div>
  </section>

  <section class="card card--back" aria-label="Card contact side">
    <ul class="contact-list">
      <li>Name Surname:</li>
      <li>Title: Solutions Specialist</li>
      <li>Phone:</li>
      <li>Mobile Phone :</li>
      <li>Email :</li>
      <li>website :</li>
    </ul>
    <div class="brand-mini">
      <span class="brand-mini__dot" aria-hidden="true"></span>
      <span class="brand-mini__name">Fernbrook<br>Dwellings</span>
    </div>
    <div class="card__band"></div>
  </section>
</main>
</body>
</html>
```